2-sided DIN A5 flyer for Real Estate company

Please read carefully: - Flyers should be in A5, 2-sided - Design should be eye-catching but still looking serious and trustful, modern, fresh, clean - The flyer will be sent to households. On the flyer it says that people can earn money. So the flyer should be animate people to contact me and share information with me. - The text you can use is written in «text». Please use different font sizes. Fontsize indication is written in front of «text». I would like to be able to do this in the future. I would like to be able to do this. * Update afterfirst designs I received * If you use pictures, keep in mind the reader of the flyer will not sell me a house, he will sell me a contact. So it is worth the money to pay for the money. If you use money, please use swiss currency money picture! But overall the text should be in the focus, especially on front side! The logo of my company is not too important! Front side: - Logo - Eye-catching design using the color theme of logo, not just one background color, maybe different blues - The text should be in the focus and as big as possible. Play with different sizes, bold / unbold, capital letters, etc. The goal should be that the text is the first thing that the reader see. - Dont use too many pictures. If so, you can use a graphical for tip (ie light bubble) in front of a real estate, then an equal sign and then a graphical for money or incentive. Cause thats what they get. - Big-font: «Your tip is us up to CHF 3 '- Big-font:« Big-font: 500.- worth! »- Phone icon, medium-font:« 044 618 53 90 »- Mail icon, medium-font:« ch@valdorf-immo.ch »- Website icon, medium-font:« www.valdorf- Immo.ch »Back side: Big-font:« Your tip is worth MONEY! "Medium-font:" You know a potential real estate salesman in your family, friends, acquaintances, club or professional world? Whether immediate or in the near future your tip can pay off for you. After a successful placement we will give you a tip-and-shoot commission of up to CHF 3'500 .-- »Medium-font. «And as simple as this works: 1. You contact us and give us the willing owner 2. We contact the owner and conclude a brokerage from 3. We start the sales process and inform you about the progress 4. After you have successfully completed your sales contract, you will receive your donor commission! »Medium-font. «Example: Thanks to your tip we can sell a property to 1.5 million. Your donor commission is CHF 3'000 .-- (0.2% of CHF 1'500'000.-) »Medium-font. "Valdorf Immobilien Treuhand AG Lindmattweg 14 8053 Zürich" - Phone icon, medium-font: «044 618 53 90» - Mail icon, medium-font: «ch@valdorf-immo.ch» - Website icon, medium-font: « Www.valdorf-immo.ch "Very-small-font at bottom of flyer" * The Tippgeberprovision is paid out after the public noti fi cation of the purchase contract as well as after receipt of the mediation commission. The donor commission is 0.2% of the selling price, but the maximum is CHF 3'500 .--. In the event of non-compliance with our mediation commission, payment of the donor commission can not be made. The donor guaranty is only paid once per object and only applies to objects that are not known to us at the time of your contact. We reserve the right to refuse, at our own discretion, any objects, owners or operators. The legal process is excluded. »

Target Market(s)

Every household

Industry/Entity Type

Real Estate

Font styles to use
Serif
Sans Serif

Colors
0255a3
3277b5
33a6d7
85cae6
cfdfed
0692cd

Requirements
Must have
• See project description

```html
<!DOCTYPE html>
<html lang="de">
<head>
<meta charset="utf-8">
<title>Valdorf Immobilien – Tippgeber Flyer</title>
<link rel="stylesheet" href="https://fonts.googleapis.com/css2?family=Montserrat:wght@700;800&family=Cabin:wght@400;500;600&family=Tinos&display=swap">
<style>
  :root {
    --navy: #0255a3;
    --mid-blue: #3277b5;
    --sky: #33a6d7;
    --light-sky: #85cae6;
    --pale: #cfdfed;
    --bright: #0692cd;
    --ink: #2f3033;
    --grey-text: #6b6e72;
    --silver: #d3d8dd;
    --dark-bar: #3a3b3e;
    --backdrop: #e7e5e2;
  }
  * { box-sizing: border-box; margin: 0; padding: 0; }
  html, body { width: 1200px; height: 858px; overflow: hidden; }
  body { background: var(--backdrop); position: relative; font-family: "Cabin", sans-serif; }

  .flyer { position: absolute; top: 90px; width: 470px; height: 668px; background: #fff; overflow: hidden; box-shadow: 0 3px 10px rgba(0,0,0,.25); }
  .flyer--front { left: 80px; }
  .flyer--back { left: 623px; }
  .flyer > * { position: absolute; }
  .backdrop-svg { left: 0; top: 0; }

  /* front */
  .photo-keys { left: 0; top: 0; width: 470px; height: 240px; background: linear-gradient(160deg, #f4f5f6 0%, #e4e7ea 55%, #cfd5da 100%); }
  .photo-woman { left: 140px; top: 420px; width: 145px; height: 248px; border-radius: 70px 70px 0 0; background: linear-gradient(180deg, #e2b77a 0%, #eccaa8 40%, #d9c6b4 75%, #b7c1c6 100%); }
  .question { left: 352px; top: 178px; font-family: "Montserrat", sans-serif; font-weight: 800; font-size: 150px; line-height: 1; color: var(--sky); }
  .front-headline { left: 27px; top: 250px; font-family: "Montserrat", sans-serif; font-weight: 700; font-size: 31px; line-height: 38px; color: #fff; text-shadow: 0 1px 4px rgba(0,0,0,.25); letter-spacing: .5px; }
  .front-sub { left: 27px; top: 330px; font-size: 19.5px; line-height: 24px; font-weight: 500; color: #fff; }
  .bag-badge { left: 45px; top: 425px; }
  .bag-caption { left: 12px; top: 496px; width: 130px; text-align: center; font-family: "Tinos", serif; font-size: 11.5px; line-height: 13.5px; color: #fff; }
  .front-brand { left: 291px; top: 440px; width: 150px; text-align: center; font-family: "Montserrat", sans-serif; font-weight: 700; font-size: 27px; color: var(--ink); letter-spacing: 2px; }
  .front-address { left: 287px; top: 499px; font-size: 11px; line-height: 13px; color: #1f2023; }
  .contact-list { left: 288px; top: 530px; list-style: none; }
  .contact-list li { display: flex; align-items: center; gap: 11px; height: 21px; font-size: 14.5px; color: var(--grey-text); }
  .contact-list svg { flex: none; }
  .phone-bar { left: 280px; top: 600px; width: 190px; height: 54px; background: var(--dark-bar); display: flex; align-items: center; justify-content: center; gap: 8px; font-size: 22px; font-weight: 600; color: #fff; }

  /* back */
  .back-title { left: 19px; top: 29px; color: var(--navy); font-weight: 600; }
  .back-title .line1 { font-size: 21.5px; line-height: 25px; display: block; }
  .back-title .line2 { font-size: 18px; line-height: 21px; display: block; }
  .back-brand { left: 332px; top: 44px; width: 125px; text-align: center; font-family: "Montserrat", sans-serif; font-weight: 700; font-size: 22px; color: var(--ink); letter-spacing: 1.5px; }
  .back-intro { left: 19px; top: 87px; width: 437px; font-size: 10.3px; line-height: 13.4px; color: var(--grey-text); text-align: justify; }
  .photo-people { left: 0; top: 0; }
  .example-badge { left: 296px; top: 287px; width: 148px; height: 148px; border-radius: 50%; background: radial-gradient(circle at 40% 35%, #ffffff 0%, #eef2f5 60%, #c9d1d8 100%); box-shadow: 0 3px 8px rgba(0,0,0,.35); display: flex; flex-direction: column; align-items: center; justify-content: center; text-align: center; padding: 0 14px; font-family: "Tinos", serif; font-size: 10.3px; line-height: 12.2px; color: var(--navy); }
  .steps-tab { left: 0; top: 415px; width: 208px; height: 27px; background: #fff; border-radius: 0 14px 14px 0; box-shadow: 0 2px 5px rgba(0,0,0,.25); padding-left: 19px; font-size: 12.5px; line-height: 27px; color: var(--ink); }
  .steps { left: 18px; top: 452px; list-style: none; }
  .steps li { display: flex; align-items: center; gap: 7px; height: 22.6px; font-size: 11.4px; color: #fff; }
  .contact-pill { left: 22px; top: 567px; width: 434px; height: 38px; background: linear-gradient(#ffffff, #e9ecef); border-radius: 19px; box-shadow: 0 2px 5px rgba(0,0,0,.3); display: flex; align-items: center; justify-content: space-around; padding: 0 10px; font-size: 11.8px; font-weight: 500; color: var(--grey-text); }
  .contact-pill span { display: flex; align-items: center; gap: 7px; }
  .disclaimer { left: 18px; top: 617px; width: 436px; font-size: 5.9px; line-height: 7.9px; color: #333; text-align: justify; }
</style>
</head>
<body>

<!-- Front side -->
<section class="flyer flyer--front">
  <div class="photo-keys" role="img" aria-label="Photo: a hand holding a small model house and a set of keys"></div>
  <svg class="backdrop-svg" width="470" height="668" viewBox="0 0 470 668" aria-hidden="true">
    <defs>
      <linearGradient id="frontBlue" x1="0" y1="0" x2="1" y2="1">
        <stop offset="0" stop-color="#0692cd"/>
        <stop offset=".55" stop-color="#3277b5"/>
        <stop offset="1" stop-color="#0255a3"/>
      </linearGradient>
      <linearGradient id="frontWhite" x1="0" y1="0" x2="0" y2="1">
        <stop offset="0" stop-color="#ffffff"/>
        <stop offset="1" stop-color="#e3e6e9"/>
      </linearGradient>
    </defs>
    <path d="M0,212 C150,190 330,220 458,336 L470,336 L470,0 L470,336" fill="none"/>
    <path d="M0,216 C150,196 320,226 452,336 L470,336 L470,668 L0,668 Z" fill="#d7dce0"/>
    <path d="M0,224 C150,204 312,232 440,336 L470,336 L470,668 L0,668 Z" fill="url(#frontBlue)"/>
    <path d="M135,668 C165,470 320,345 470,330 L470,668 Z" fill="var(--silver)"/>
    <path d="M145,668 C175,478 325,355 470,340 L470,668 Z" fill="url(#frontWhite)"/>
  </svg>
  <div class="photo-woman" role="img" aria-label="Photo: smiling woman holding a fan of Swiss franc banknotes"></div>
  <div class="question">?</div>
  <h1 class="front-headline">WIR BEZAHLEN<br>FÜR IHREN TIPP!</h1>
  <p class="front-sub">Sie kennen jemanden, der sein<br>Haus oder seine Wohnung<br>verkaufen will?</p>
  <svg class="bag-badge" width="62" height="62" viewBox="0 0 62 62" aria-hidden="true">
    <circle cx="31" cy="31" r="30" fill="#fff"/>
    <circle cx="31" cy="31" r="26" fill="#4a4b4e"/>
    <path d="M25,20 L37,20 L34,25 C41,28 44,35 43,40 C42,44 38,45 31,45 C24,45 20,44 19,40 C18,35 21,28 28,25 Z" fill="#fff"/>
    <text x="31" y="40" text-anchor="middle" font-family="Cabin, sans-serif" font-size="11" font-weight="600" fill="#4a4b4e">€</text>
  </svg>
  <p class="bag-caption">Ihr Tipp ist uns bis<br>zu CHF 3'500.- wert!</p>
  <div class="front-brand">VALDORF</div>
  <p class="front-address">Valdorf Immobilien + Treuhand AG<br>Lindmattweg 14, 8053 Zürich</p>
  <ul class="contact-list">
    <li><svg width="13" height="13" viewBox="0 0 13 13"><rect width="13" height="13" rx="2" fill="var(--mid-blue)"/><path d="M4,3 L5.5,3 L6,5 L5,5.8 C5.5,7 6,7.5 7.2,8 L8,7 L10,7.5 L10,9 C7,9.5 3.5,6 4,3 Z" fill="#fff"/></svg>044 618 53 90</li>
    <li><svg width="13" height="13" viewBox="0 0 13 13"><rect width="13" height="13" rx="2" fill="var(--mid-blue)"/><rect x="3" y="4" width="7" height="5" fill="none" stroke="#fff"/><path d="M3,4 L6.5,7 L10,4" fill="none" stroke="#fff"/></svg>ch@valdorf-immo.ch</li>
    <li><svg width="13" height="13" viewBox="0 0 13 13"><rect width="13" height="13" rx="2" fill="var(--mid-blue)"/><circle cx="6.5" cy="6.5" r="3.5" fill="none" stroke="#fff"/><path d="M3,6.5 H10 M6.5,3 C5,5 5,8 6.5,10 M6.5,3 C8,5 8,8 6.5,10" fill="none" stroke="#fff" stroke-width=".7"/></svg>www.valdorf-immo.ch</li>
  </ul>
  <div class="phone-bar">
    <svg width="22" height="22" viewBox="0 0 22 22" aria-hidden="true"><path d="M4,2 L8,2 L9.5,7 L7,9 C8.3,12 10,13.7 13,15 L15,12.5 L20,14 L20,18 C11,19.5 2.5,11 4,2 Z" fill="#fff"/></svg>
    044 618 53 90
  </div>
</section>

<!-- Back side -->
<section class="flyer flyer--back">
  <svg class="photo-people" width="470" height="668" viewBox="0 0 470 668" role="img" aria-label="Photo: a young couple meeting an estate agent with a tablet in front of a house entrance">
    <defs>
      <linearGradient id="peoplePhoto" x1="0" y1="0" x2="1" y2="0">
        <stop offset="0" stop-color="#c9cdd1"/>
        <stop offset=".45" stop-color="#8d959b"/>
        <stop offset="1" stop-color="#b3a799"/>
      </linearGradient>
      <linearGradient id="backBlue" x1="0" y1="0" x2="1" y2="1">
        <stop offset="0" stop-color="#3277b5"/>
        <stop offset=".5" stop-color="#0692cd"/>
        <stop offset="1" stop-color="#0255a3"/>
      </linearGradient>
    </defs>
    <path d="M0,236 C150,180 300,150 470,143 L470,158 C300,162 150,192 0,246 Z" fill="var(--navy)"/>
    <path d="M0,246 C150,192 300,162 470,158 L470,346 C320,352 150,370 0,404 Z" fill="url(#peoplePhoto)"/>
    <path d="M0,398 C150,362 320,344 470,340 L470,352 C320,356 150,374 0,410 Z" fill="#ffffff"/>
    <path d="M0,410 C150,374 320,356 470,352 L470,590 L0,590 Z" fill="url(#backBlue)"/>
  </svg>
  <h1 class="back-title"><span class="line1">Ihr TIPP ist GELD wert!</span><span class="line2">Verraten Sie ihn uns noch heute!</span></h1>
  <div class="back-brand">VALDORF</div>
  <p class="back-intro">Sie kennen in der Familie, im Freundeskreis, im Bekanntenkreis, im Verein oder aus der Berufswelt einen potentiellen Immobilienverkäufer? Ob sofort oder in naher Zukunft kann sich Ihr Tipp für Sie auszahlen. Tippgeber erhalten von uns nach einer erfolgreichen Vermittlung eine Tippgeberprovision von bis zu CHF 3'500.</p>
  <div class="example-badge">
    <p>BEISPIEL:</p>
    <p>Dank Ihrem Tipp können wir eine Immobilie zu 1.5 Mio verkaufen.</p>
    <p>Ihre Tippgeberprovision beträgt in dem Fall CHF 3'000.-- (0.2% von CHF 1'500'000.--)</p>
  </div>
  <div class="steps-tab">Und so einfach funktionierts:</div>
  <ul class="steps">
    <li><svg width="14" height="14" viewBox="0 0 14 14"><circle cx="7" cy="7" r="6" fill="none" stroke="#fff" stroke-width="1.3"/><path d="M4,7 L6.3,9.2 L10,5" fill="none" stroke="#fff" stroke-width="1.4"/></svg>Sie kontaktieren uns und geben uns den verkaufswilligen Eigentümer an</li>
    <li><svg width="14" height="14" viewBox="0 0 14 14"><circle cx="7" cy="7" r="6" fill="none" stroke="#fff" stroke-width="1.3"/><path d="M4,7 L6.3,9.2 L10,5" fill="none" stroke="#fff" stroke-width="1.4"/></svg>Wir kontaktieren den Eigentümer und schliessen einen Maklervertrag ab</li>
    <li><svg width="14" height="14" viewBox="0 0 14 14"><circle cx="7" cy="7" r="6" fill="none" stroke="#fff" stroke-width="1.3"/><path d="M4,7 L6.3,9.2 L10,5" fill="none" stroke="#fff" stroke-width="1.4"/></svg>Wir starten den Verkaufsprozess und informieren Sie über die Fortschritte</li>
    <li><svg width="14" height="14" viewBox="0 0 14 14"><circle cx="7" cy="7" r="6" fill="none" stroke="#fff" stroke-width="1.3"/><path d="M4,7 L6.3,9.2 L10,5" fill="none" stroke="#fff" stroke-width="1.4"/></svg>Nach erfolgreichem Verkaufsabschluss erhalten Sie Ihre Tippgeberprovision!»</li>
  </ul>
  <div class="contact-pill">
    <span><svg width="11" height="11" viewBox="0 0 13 13"><rect width="13" height="13" rx="2" fill="var(--mid-blue)"/><circle cx="6.5" cy="6.5" r="3.5" fill="none" stroke="#fff"/></svg>www.valdorf-immo.ch</span>
    <span><svg width="11" height="11" viewBox="0 0 13 13"><rect width="13" height="13" rx="2" fill="var(--mid-blue)"/><path d="M4,3 L5.5,3 L6,5 L5,5.8 C5.5,7 6,7.5 7.2,8 L8,7 L10,7.5 L10,9 C7,9.5 3.5,6 4,3 Z" fill="#fff"/></svg>044 618 53 90</span>
    <span><svg width="11" height="11" viewBox="0 0 13 13"><rect width="13" height="13" rx="2" fill="var(--mid-blue)"/><rect x="3" y="4" width="7" height="5" fill="none" stroke="#fff"/><path d="M3,4 L6.5,7 L10,4" fill="none" stroke="#fff"/></svg>ch@valdorf-immo.ch</span>
  </div>
  <p class="disclaimer">Die Tippgeberprovision wird nach der öffentlichen Beurkundung des Kaufvertrags sowie nach Erhalt der Vermittlungsprovision ausbezahlt. Die Tippgeberprovision beträgt 0.2% des erzielten Verkaufspreises, im Maximum jedoch CHF 3'500.--. Bei Nichterhalt unserer Vermittlungsprovision kann auch keine Auszahlung der Tippgeberprovision erfolgen. Die Tippgeberprovision wird pro Objekt nur einmalig ausbezahlt und gilt nur für Objekte, die uns zum Zeitpunkt Ihrer Kontaktaufnahme noch nicht bekannt sind. Wir behalten uns das Recht vor nach eigenem Ermessen Objekte, Eigentümer oder Tippgeber abzulehnen. Der Rechtsweg ist ausgeschlossen.</p>
</section>

</body>
</html>
```